Power Point Template Design for Consulting Company
Verdant Ridge Inc.
Helping Clients Achieve Explosive Sales
Need a slide master incorporating existing logo for all regular Power Point slide layout types (title, title and content, section header, two content, comparison, title only, blank, content with caption, picture with caption)
Corporate client presentations and professional association speaking engagements
Using Power Point 2007, Windows 7.0 O/S.
Not overpowering, prefer clean white backgrounds for better projection and printing results. Verdant Ridge Inc. Logo was designed on a previous project so all files available.
logo files in all formats
business card for reference and consistency
business letterhead for reference and consistency
business stationary coor and font for reference and consistency

```html
<!DOCTYPE html>
<html lang="en">
<head>
<meta charset="utf-8">
<title>Verdant Ridge Inc. – Slide Master Layouts</title>
<link rel="stylesheet" href="https://fonts.googleapis.com/css2?family=Open+Sans:wght@400;600;700&display=swap">
<style>
  :root{
    --navy:#17468f;
    --blue:#2a7fcb;
    --sky:#63bdec;
    --pale:#cfeafb;
    --ink:#1f62ab;
    --grey:#8a8f94;
    --line:#c9ced3;
    --white:#ffffff;
  }
  *{box-sizing:border-box;margin:0;padding:0}
  html,body{width:1200px;height:871px;overflow:hidden;background:var(--white);font-family:"Open Sans",Arial,sans-serif}
  .sheet{position:relative;width:1200px;height:871px}

  .slide{position:absolute;width:468px;height:357px;border-radius:12px;overflow:hidden;background:var(--white);box-shadow:0 0 0 1px #e6ecf1}
  .slide--title{left:372px;top:36px}
  .slide--content{left:53px;top:449px}
  .slide--section{left:665px;top:449px}

  .slide__header{position:absolute;left:0;top:0;width:100%;height:80px}
  .slide__footer{position:absolute;left:0;bottom:0;width:100%;height:120px;
    background:linear-gradient(to top,var(--blue) 0%,var(--sky) 28%,var(--pale) 62%,rgba(255,255,255,0) 100%)}
  .slide__mark{position:absolute;right:26px;bottom:22px;width:58px;height:58px;border-radius:8px;background:rgba(255,255,255,.45)}

  .brand{position:absolute;display:flex;flex-direction:column;align-items:flex-start;gap:4px}
  .brand__square{width:34px;height:34px;background:var(--blue);border:3px solid var(--white);border-radius:3px;box-shadow:0 0 0 1px #d5e3ef}
  .brand__name{font-size:10px;font-weight:600;color:var(--navy);white-space:nowrap}
  .slide--title .brand{left:58px;top:10px}
  .slide--content .brand,.slide--section .brand{left:40px;top:6px}

  .box{position:absolute;border:1px solid var(--line);background:var(--white)}
  .title-box{left:31px;top:108px;width:406px;height:77px;display:flex;align-items:center;justify-content:center;text-align:center;
    color:var(--ink);font-weight:700;font-size:23px;line-height:1.2;text-transform:uppercase}
  .subtitle-box{left:67px;top:197px;width:334px;height:91px;text-align:center;padding-top:6px;color:var(--grey);font-size:17px}

  .heading-box{left:26px;top:101px;width:418px;height:40px;display:flex;align-items:center;justify-content:center;color:var(--ink);font-weight:700;font-size:17px}
  .body-box{left:26px;top:146px;width:418px;height:144px;padding:6px 10px;font-size:13px;color:#222}
  .body-box li{margin-left:14px}
  .insert-icons{position:absolute;left:146px;top:40px;display:grid;grid-template-columns:repeat(3,26px);gap:12px 10px}
  .insert-icons svg{width:26px;height:26px}

  .section-text{left:31px;top:151px;width:408px;height:77px;display:flex;align-items:flex-end;padding:0 4px 3px;font-size:10px;color:#333}
  .section-title{left:31px;top:228px;width:408px;height:74px;padding:4px 6px;color:var(--grey);font-weight:700;font-size:18px;text-transform:uppercase}

  .caption{position:absolute;width:468px;text-align:center;color:var(--ink);font-weight:700;font-size:13px;letter-spacing:.3px}
  .caption--title{left:372px;top:404px}
  .caption--content{left:53px;top:822px}
  .caption--section{left:665px;top:822px}
</style>
</head>
<body>
<main class="sheet">

  <svg width="0" height="0" style="position:absolute">
    <defs>
      <linearGradient id="band" x1="0" x2="1" y1="0" y2="0">
        <stop offset="0" stop-color="#8fd2f3"/>
        <stop offset=".45" stop-color="#2f8ad2"/>
        <stop offset="1" stop-color="#17468f"/>
      </linearGradient>
      <symbol id="header-band" viewBox="0 0 468 80" preserveAspectRatio="none">
        <path d="M0 0H468V30C360 32 210 34 130 40C110 42 100 56 96 64H0Z" fill="url(#band)"/>
        <path d="M96 64C100 56 110 46 130 44C210 40 360 38 468 38V42C360 42 210 44 132 48C114 50 104 58 100 66Z" fill="#2a7fcb" opacity=".55"/>
      </symbol>
    </defs>
  </svg>

  <!-- Title layout -->
  <section class="slide slide--title">
    <svg class="slide__header" aria-hidden="true"><use href="#header-band"/></svg>
    <div class="slide__footer"></div>
    <div class="slide__mark"></div>
    <div class="brand"><span class="brand__square"></span><span class="brand__name">Verdant Ridge Inc.</span></div>
    <div class="box title-box">Click to edit master<br>title style</div>
    <div class="box subtitle-box">Click to add subtitle</div>
  </section>
  <p class="caption caption--title">TITLE</p>

  <!-- Title and content layout -->
  <section class="slide slide--content">
    <svg class="slide__header" aria-hidden="true"><use href="#header-band"/></svg>
    <div class="slide__footer"></div>
    <div class="slide__mark"></div>
    <div class="brand"><span class="brand__square"></span><span class="brand__name">Verdant Ridge Inc.</span></div>
    <div class="box heading-box">Click to add title</div>
    <div class="box body-box">
      <ul><li>Click to add text</li></ul>
      <div class="insert-icons" aria-hidden="true">
        <svg viewBox="0 0 26 26"><rect x="2" y="4" width="22" height="18" fill="#e8eef4" stroke="#9aa7b3"/><path d="M2 10H24M2 16H24M9 4V22M17 4V22" stroke="#9aa7b3"/></svg>
        <svg viewBox="0 0 26 26"><rect x="4" y="12" width="5" height="10" fill="#4f86c6"/><rect x="11" y="6" width="5" height="16" fill="#6aa84f"/><rect x="18" y="10" width="5" height="12" fill="#e39b3b"/></svg>
        <svg viewBox="0 0 26 26"><rect x="9" y="3" width="8" height="6" fill="#7fb0de"/><rect x="2" y="16" width="8" height="6" fill="#7fb0de"/><rect x="16" y="16" width="8" height="6" fill="#7fb0de"/><path d="M13 9V13H6V16M13 13H20V16" stroke="#7b8a97" fill="none"/></svg>
        <svg viewBox="0 0 26 26"><rect x="2" y="5" width="22" height="16" fill="#dbe9f5" stroke="#9aa7b3"/><path d="M3 20L10 12L15 17L18 14L23 20Z" fill="#5e9bd0"/></svg>
        <svg viewBox="0 0 26 26"><rect x="4" y="3" width="18" height="20" fill="#f1f4f7" stroke="#9aa7b3"/><circle cx="13" cy="12" r="5" fill="#8fb7db"/></svg>
        <svg viewBox="0 0 26 26"><rect x="3" y="3" width="20" height="20" fill="#eef1f4" stroke="#9aa7b3"/><rect x="7" y="7" width="12" height="12" fill="#b9c4ce"/></svg>
      </div>
    </div>
  </section>
  <p class="caption caption--content">TITLE AND CONTENT</p>

  <!-- Section header layout -->
  <section class="slide slide--section">
    <svg class="slide__header" aria-hidden="true"><use href="#header-band"/></svg>
    <div class="slide__footer"></div>
    <div class="slide__mark"></div>
    <div class="brand"><span class="brand__square"></span><span class="brand__name">Verdant Ridge Inc.</span></div>
    <div class="box section-text">Click to add text</div>
    <div class="box section-title">Click to add title</div>
  </section>
  <p class="caption caption--section">SECTION HEADER</p>

</main>
</body>
</html>
```